we need a postcard design for our new company,
Marigold Wedding & Events.

I have attached our logo and 2 pictures I would like to utilise on the card if poss, definately use the logo.

Industry/Entity Type

It Company

Requirements
Must have
• Ph no. 5371 2608 ( just the number will do)

info@marigoldweddingsandevents.example.au

Wedding & Event Hire /Styling all over Melbourne, South East Suburbs, The Penninsula, The Dandenongs, Phillip Island & Gippsland.

```html
<!DOCTYPE html>
<html lang="en">
<head>
<meta charset="utf-8">
<title>Marigold Wedding &amp; Events – Postcard</title>
<link rel="stylesheet" href="https://fonts.googleapis.com/css2?family=Lobster+Two:ital,wght@1,700&family=Oswald:wght@300;400&display=swap">
<style>
  :root {
    --purple: #5b2a86;
    --ink: #1a1a1a;
    --paper: #ffffff;
    --paper-tint: #f4f3f5;
    --band: #0d0d0d;
    --band-text: #ffffff;
  }
  html, body {
    margin: 0;
    padding: 0;
    overflow: hidden;
    background: var(--paper);
  }
  .postcard {
    position: relative;
    width: 924px;
    height: 1200px;
    overflow: hidden;
    background: radial-gradient(ellipse at 50% 30%, var(--paper) 0%, var(--paper-tint) 100%);
    font-family: "Oswald", "Arial Narrow", sans-serif;
    color: var(--ink);
  }
  .brand {
    position: absolute;
    left: 92px;
    top: 48px;
    margin: 0;
    font-family: "Lobster Two", cursive;
    font-style: italic;
    font-weight: 700;
    color: var(--purple);
    line-height: 1;
  }
  .brand-name {
    display: block;
    font-size: 124px;
  }
  .brand-sub {
    display: block;
    margin-top: 10px;
    margin-left: 140px;
    font-size: 34px;
  }
  .tagline {
    position: absolute;
    left: 0;
    width: 100%;
    top: 306px;
    margin: 0;
    text-align: center;
    font-family: "Lobster Two", cursive;
    font-style: italic;
    font-weight: 700;
    font-size: 50px;
    color: var(--purple);
  }
  .coverage {
    position: absolute;
    left: 46px;
    top: 404px;
    width: 850px;
    margin: 0;
    font-weight: 400;
    font-size: 29px;
    line-height: 44px;
  }
  .services-title {
    position: absolute;
    left: 46px;
    top: 526px;
    margin: 0;
    font-weight: 300;
    font-size: 32px;
  }
  .services {
    position: absolute;
    left: 60px;
    top: 594px;
    margin: 0;
    padding: 0 0 0 42px;
    font-weight: 300;
    font-size: 23px;
    line-height: 36.6px;
  }
  .photo {
    position: absolute;
    left: 420px;
    top: 510px;
    width: 680px;
    height: 680px;
    border-radius: 50%;
    background:
      radial-gradient(circle at 62% 30%, #fbfaf2 0%, #ecebd9 18%, transparent 34%),
      radial-gradient(circle at 50% 62%, #e9ecea 0%, transparent 40%),
      linear-gradient(160deg, #5c6a52 0%, #2f3a2c 45%, #b9bfb3 75%, #6f7d6a 100%);
  }
  .footer {
    position: absolute;
    left: 0;
    bottom: 0;
    width: 100%;
    height: 83px;
    background: var(--band);
    color: var(--band-text);
    font-family: "Lobster Two", cursive;
    font-style: italic;
    font-weight: 700;
    font-size: 31px;
  }
  .footer-email {
    position: absolute;
    left: 27px;
    top: 20px;
  }
  .footer-phone {
    position: absolute;
    right: 28px;
    top: 20px;
  }
</style>
</head>
<body>
  <main class="postcard">
    <h1 class="brand">
      <span class="brand-name">Marigold</span>
      <span class="brand-sub">Wedding &amp; Events</span>
    </h1>

    <p class="tagline">Every wedding and event is unique</p>

    <p class="coverage">Wedding &amp; Event Hire /Styling all over Melbourne, South East Suburbs, The Penninsula, The Dandenongs, Phillip Island &amp; Gippsland</p>

    <h2 class="services-title">Our services include</h2>
    <ul class="services">
      <li>Beach &amp; Garden Weddings</li>
      <li>Americana Chairs</li>
      <li>Wedding Arches</li>
      <li>Market &amp; Golf Umbrellas</li>
      <li>Carpet Runners</li>
      <li>Chaircovers &amp; Sashes</li>
      <li>Table Linen</li>
      <li>Lolly Buffet</li>
      <li>Wishing Wells</li>
      <li>Ceiling Draping</li>
      <li>Bridal Flowers</li>
      <li>Delivery, Set Up &amp; Pack Down</li>
    </ul>

    <div class="photo" role="img" aria-label="Close-up photo of a white rose with baby's breath and greenery"></div>

    <footer class="footer">
      <span class="footer-email">info@marigoldweddingsandevents.example.au</span>
      <span class="footer-phone">Call us: 5371 2608</span>
    </footer>
  </main>
</body>
</html>
```